New Orleans history and Study Guide for Professional Tour Guide - City of New Orleans

Book cover. Paperback, 5.25” x 8” book cover, 172 pages, White paper, PageMill template – attached. (PageMill names the template as 180 pages)

This book puts the history of New Orleans into easy sections for persons to learn who are preparing to take the test for the City of New Orleans Certified Visitor Escort Permit. It is required of all tour guides in the city. The attached text for the back cover gives a more complete synopsis of the content.

This Study Guide is a resource for persons seeking a tour guide license. We would like the cover to reflect the professionalism required for test preparation and carry a subtle connection to the creativity of the author as a storyteller and entertainer in the city of New Orleans.

An idea we have had for the front cover would have a background of stylized map of the famed Marigot Ward in the lower half of the cover. Possibly a fan shaped perspective view. The central focus of the Marigot Ward, and the city, is St. Aubin Basilica and Harwell Plaza as seen in these maps and images. https://lnk.example/q7TzWa Maps old and new - https://lnk.example/v3RbYe. A map is not a requirement for cover. Creativity is.

Attached is PageMill/Brindle template, text for front and back cover and two photographs of the author for you to choose from. Both need photoshopping to remove persons behind or next Mr Calloway.

Authors’ previous book: 'Out Along the Levee: Tall Tales of a Storied Port' by Edmund Calloway Link: http://bk.example/7Q2MVXT

Target Market(s)

Persons 18+

Industry/Entity Type

Tourism

Font styles to use
Serif

Requirements
Must have
• Design with book front and back cover with: spine.
• Primary Title is : Study Guide for Professional Tour Guide License Test
• Sub-title: City of New Orleans
Nice to have
• Possible image for design is a Fleur-de-lis, an official emblem of New Orleans. This is a design option and not .a serious Nice To Have.. Some inspiration https://lnk.example/k9DuPx

```html
<!DOCTYPE html>
<html lang="en">
<head>
<meta charset="utf-8">
<title>Study Guide for the Professional Tour Guide Test – Cover</title>
<link href="https://fonts.googleapis.com/css2?family=Cinzel:wght@400;500&family=Source+Sans+3:wght@400;700;800&display=swap" rel="stylesheet">
<style>
:root{
  --ink:#111;
  --title-red:#8e2a2c;
  --title-navy:#14284a;
  --back-top:#ffffff;
  --back-bottom:#a9cde8;
  --spine:#b9d6ee;
  --sky-top:#9fc3e2;
  --sky-mid:#e6eef4;
  --sky-low:#b9d0e4;
  --photo-frame:#f1b9a0;
  --author-blue:#1e2e5a;
}
*{margin:0;padding:0;box-sizing:border-box}
html,body{width:1200px;height:887px;overflow:hidden;background:#fff}
.cover{position:relative;width:1200px;height:887px;font-family:"Source Sans 3",sans-serif;color:var(--ink)}
.back{position:absolute;left:0;top:0;width:565px;height:887px;background:linear-gradient(180deg,var(--back-top) 0%,#dcecf8 35%,var(--back-bottom) 100%)}
.spine{position:absolute;left:565px;top:0;width:71px;height:887px;background:linear-gradient(180deg,#e4f0fa,var(--spine))}
.front{position:absolute;left:636px;top:0;width:564px;height:887px;overflow:hidden;background:linear-gradient(180deg,var(--sky-top) 0%,var(--sky-mid) 35%,#f2f5f7 55%,var(--sky-low) 75%)}

.kicker{font-family:"Source Sans 3",sans-serif;font-weight:700;letter-spacing:.42em;text-align:center;white-space:nowrap}
.title{font-weight:800;text-align:center;line-height:1.05;letter-spacing:-.01em;white-space:nowrap}
.city{font-family:"Cinzel",serif;text-align:center;white-space:nowrap}

.back .kicker{position:absolute;left:0;width:565px;top:34px;font-size:27px}
.back .title{position:absolute;left:0;width:565px;top:70px;font-size:53px;color:var(--title-red);transform:scaleX(.92)}
.back .city{position:absolute;left:0;width:565px;top:186px;font-size:28px}
.back .city small{font-size:19px}

.author-photo{position:absolute;left:40px;top:244px;width:268px;height:216px;border:2px solid var(--photo-frame);background:linear-gradient(180deg,#8a8a7c 0%,#a38a6e 45%,#b06a3e 80%,#6b5a48 100%)}
.blurb{position:absolute;font-size:13.6px;line-height:18px;text-align:justify}
.blurb p{text-indent:6px;margin-bottom:5px}
.blurb-left{left:38px;top:478px;width:272px}
.blurb-right{left:331px;top:240px;width:212px}

.spine-line{position:absolute;transform-origin:0 0;transform:rotate(90deg);white-space:nowrap}
.spine-kicker{left:622px;top:38px;font-size:21px;font-weight:700;letter-spacing:.53em}
.spine-title{left:595px;top:38px;font-size:20px;font-weight:800;letter-spacing:-.01em}
.spine-author{left:614px;top:455px;font-family:"Cinzel",serif;font-size:27px;color:var(--author-blue)}

.front .author{position:absolute;left:0;width:564px;top:30px;text-align:center;font-family:"Cinzel",serif;font-size:34px;white-space:nowrap}
.front .kicker{position:absolute;left:0;width:564px;top:149px;font-size:28px}
.front .title{position:absolute;left:0;width:564px;top:190px;font-size:58px;color:var(--title-navy);transform:scaleX(.92)}
.front .city{position:absolute;left:0;width:564px;top:370px;font-size:35px;line-height:1}
.front .city span{display:block;font-size:52px;margin-top:6px}
.cityscape{position:absolute;left:0;top:560px;width:564px;height:327px}
</style>
</head>
<body>
<div class="cover">
  <section class="back">
    <div class="kicker">STUDY GUIDE FOR</div>
    <h2 class="title">THE PROFESSIONAL<br>TOUR GUIDE TEST</h2>
    <div class="city"><small>CITY OF</small> NEW ORLEANS</div>
    <div class="author-photo" role="img" aria-label="Portrait photograph of the author in a flat cap and sunglasses"></div>
    <div class="blurb blurb-left">
      <p>This <b>STUDY GUIDE</b> is designed to prepare a person for the City of New Orleans Certified Visitor Escort Permit test. Laid out in simple, easy to learn sections this is the basic information needed for passing the city test and moving on to becoming an entertaining tour guide. Your knowledge of the history of New Orleans and Louisiana is key to earning money as a professional tour guide. Tips are directly related to the quality of your stories.</p>
      <p>This guide names the important people, places and events of the city. Recommended readings are based on the author’s own personal preferences for reference or pleasure reading.</p>
    </div>
    <div class="blurb blurb-right">
      <p>A special feature included is a seasoned written Marigot Ward Walking Tour complete with route, stops and full stories. The tour begins at the river and proceeds through a section of the Ward favored among tour guides. It is the bread and butter of Marigot Ward tours.</p>
      <p>Ed Calloway worked as a tour guide in the City for years. He taught the Professional Tourguiding class at Bayside Community College, plus a class in Research and Storytelling. He is an avid reader of local history. He earned a Ph.D. from Pacific Crest University in Communication, plus BA and MA degrees from Gulf State in Public Speaking.</p>
      <p>A companion to this STUDY GUIDE is Dr. Calloway’s OUT ALONG THE LEVEE – Tall Tales of a Storied Port.</p>
    </div>
  </section>

  <section class="spine">
  </section>
  <div class="spine-line spine-kicker">STUDY GUIDE FOR</div>
  <div class="spine-line spine-title">THE PROFESSIONAL TOUR GUIDE TEST</div>
  <div class="spine-line spine-author">EDMUND C CALLOWAY JR., PHD</div>

  <section class="front">
    <div class="author">EDMUND C CALLOWAY JR., PHD</div>
    <div class="kicker">STUDY GUIDE FOR</div>
    <h1 class="title">THE PROFESSIONAL<br>TOUR GUIDE TEST</h1>
    <div class="city">CITY OF<span>NEW ORLEANS</span></div>
    <svg class="cityscape" viewBox="0 0 564 327" role="img" aria-label="Wide-angle aerial photograph of St. Aubin Basilica and Harwell Plaza in the Marigot Ward">
      <defs>
        <linearGradient id="town" x1="0" y1="0" x2="0" y2="1">
          <stop offset="0" stop-color="#9a9c9a"/>
          <stop offset=".45" stop-color="#8d7f72"/>
          <stop offset=".8" stop-color="#6f7a5a"/>
          <stop offset="1" stop-color="#4d6b3a"/>
        </linearGradient>
      </defs>
      <path d="M0 95 Q282 30 564 95 L564 327 L0 327 Z" fill="url(#town)"/>
    </svg>
  </section>
</div>
</body>
</html>
```